Need CATCHY/VIVID Banner design for my new UTV/ATV/Off Road Vehicle turn signal/lighting company

I need a banner ad designed so I can advertise on several different ATV (all terrain vehicle), UTV (Utility Vehicles), Golf Cart and Off-Road Vehicle forums. Ads need to be very catchy and produce a call to action. Action is getting hits to my website. Our main business is selling turn signal kits to make your side by side or your ATV/UTV street legal, as some states now allow you to drive these on public roads if you have the following items: Turn Signals, Horn, Lighted license plate bracket, headlights and brake lights. We sell all of these items for just about any model vehicle out there. Our call to action for this banner would be to get more website visits.

Target Market(s)

Off-road/outdoor enthusiasts,

Industry/Entity Type

Car Accessorie

Font styles to use
Sans Serif

Requirements
Must have
• Ad size need to be either 728x90 or 300x250. Colorful ad with an off-road vehicle integrated to the design (think UTV, side-by-side, etc.
Nice to have
• Nice to haves would be anything that makes this banner ad stand out on very boring web pages.
Should not have
• anything dull

```html
<!DOCTYPE html>
<html lang="en">
<head>
<meta charset="UTF-8">
<title>Trailmark Turn Signal Kits Banner</title>
<link rel="stylesheet" href="https://fonts.googleapis.com/css2?family=Archivo+Black&display=swap">
<style>
  :root {
    --sky-top: #5f6c7a;
    --sky-low: #a9b8c8;
    --sea-deep: #1f5f9e;
    --sea-light: #3f86c4;
    --rock-dark: #1b1c1e;
    --rock-mid: #3a3c40;
    --vehicle-red: #e4452a;
    --vehicle-body: #c9c4b6;
    --vehicle-dark: #2a2b2e;
    --brand-red: #e0141e;
    --ink: #111214;
    --white: #ffffff;
  }
  * { margin: 0; padding: 0; box-sizing: border-box; }
  html, body {
    width: 1200px;
    height: 400px;
    overflow: hidden;
    background: var(--white);
  }
  .banner {
    position: relative;
    width: 1200px;
    height: 400px;
    overflow: hidden;
    font-family: "Archivo Black", "Arial Black", sans-serif;
  }
  .scene {
    position: absolute;
    inset: 0;
    background:
      linear-gradient(180deg,
        var(--sky-top) 0%,
        var(--sky-low) 36%,
        var(--sea-light) 39%,
        var(--sea-deep) 55%,
        var(--rock-mid) 70%,
        var(--rock-dark) 100%);
  }
  .vehicle {
    position: absolute;
    left: 76px;
    top: 36px;
    width: 480px;
    height: 350px;
    border-radius: 40px 60px 30px 30px;
    background:
      linear-gradient(180deg,
        var(--vehicle-red) 0%,
        #c8553d 22%,
        var(--vehicle-body) 45%,
        #8c8a84 66%,
        var(--vehicle-dark) 82%,
        #161618 100%);
    box-shadow: 0 16px 30px rgba(0, 0, 0, 0.45);
  }
  .promo {
    position: absolute;
    left: 636px;
    top: 50px;
    width: 440px;
    display: flex;
    flex-direction: column;
    align-items: center;
    text-align: center;
  }
  .brand-name {
    display: flex;
    align-items: center;
    gap: 12px;
    height: 138px;
    font-size: 50px;
    line-height: 1;
    color: var(--brand-red);
    letter-spacing: 0.5px;
  }
  .brand-mark {
    width: 34px;
    height: 34px;
    background: var(--brand-red);
  }
  .headline {
    margin-top: 6px;
    font-size: 38px;
    line-height: 1;
    color: var(--ink);
    letter-spacing: 0;
    font-weight: 400;
    white-space: nowrap;
  }
  .subline {
    margin-top: 8px;
    font-size: 26px;
    line-height: 1;
    color: var(--ink);
    letter-spacing: 1.4px;
    font-weight: 400;
    white-space: nowrap;
  }
  .shop-button {
    position: absolute;
    left: 710px;
    top: 292px;
    width: 290px;
    height: 54px;
    display: flex;
    align-items: center;
    justify-content: center;
    background: var(--brand-red);
    border-radius: 7px;
    color: var(--white);
    font-size: 31px;
    text-decoration: none;
    letter-spacing: 0.2px;
  }
</style>
</head>
<body>
  <div class="banner">
    <div class="scene" role="img" aria-label="Photo of dark volcanic rock above a blue ocean coastline under a cloudy sky"></div>
    <div class="vehicle" role="img" aria-label="Photo of a grey and red sport side-by-side UTV with a red roll cage and yellow headlights, parked on the rocks"></div>

    <div class="promo">
      <div class="brand-name"><span class="brand-mark"></span>TRAILMARK</div>
      <h1 class="headline">TURN SIGNAL KITS</h1>
      <h2 class="subline">&amp; LIGHTING ACCESSORIES</h2>
    </div>

    <a class="shop-button" href="#">SHOP NOW</a>
  </div>
</body>
</html>
```